Business cards and stationary
Pepa Ruvel's Charred Relish
Bright & Fun-filled
Howard Pellingham
P. O Box 7413
Dunmore Vale, CA, 90417
855-PEPA-RUV (855-737-2788)
howard@CharredRelish.com
www.CharredRelish.com
I will upload my logo in AI format. Please choose the color scheme accordingly.
Salsa. It's not just for chips anymore!

```html
<!DOCTYPE html>
<html lang="en">
<head>
<meta charset="utf-8">
<title>Pepa Ruvel's Charred Relish – Business Card</title>
<link href="https://fonts.googleapis.com/css2?family=Cabin:wght@400;700&display=swap" rel="stylesheet">
<style>
  :root {
    --backdrop: #e9e6e1;
    --card: #ffffff;
    --red: #e2231a;
    --green: #2f9e44;
    --ink: #3a3a3a;
    --rule: #9a9a9a;
  }
  html, body {
    margin: 0;
    width: 1200px;
    height: 780px;
    overflow: hidden;
    background: var(--backdrop);
    font-family: "Cabin", sans-serif;
  }
  .card {
    position: absolute;
    left: 60px;
    top: 70px;
    width: 1080px;
    height: 640px;
    background: var(--card);
    border-radius: 34px;
    overflow: hidden;
    box-shadow: 0 6px 24px rgba(0,0,0,0.18);
  }
  .brand {
    position: absolute;
    top: 110px;
    left: 0;
    width: 100%;
    display: flex;
    justify-content: center;
    align-items: center;
    gap: 22px;
  }
  .brand-mark {
    width: 46px;
    height: 46px;
    background: var(--red);
  }
  .brand-name {
    font-weight: 700;
    font-size: 56px;
    color: var(--red);
    margin: 0;
    line-height: 1;
  }
  .holder {
    position: absolute;
    top: 345px;
    right: 560px;
    text-align: right;
    color: var(--ink);
  }
  .holder-name {
    font-weight: 700;
    font-size: 34px;
    color: var(--red);
    margin: 0 0 24px;
    white-space: nowrap;
  }
  .holder-address {
    font-size: 23px;
    line-height: 1.4;
    margin: 0;
    white-space: nowrap;
  }
  .divider {
    position: absolute;
    left: 540px;
    top: 330px;
    width: 1px;
    height: 155px;
    background: var(--rule);
  }
  .contacts {
    position: absolute;
    left: 558px;
    top: 328px;
    margin: 0;
    padding: 0;
    list-style: none;
    color: var(--ink);
    font-size: 23px;
  }
  .contacts li {
    display: flex;
    align-items: center;
    gap: 12px;
    height: 39px;
    white-space: nowrap;
  }
  .contacts svg {
    width: 22px;
    height: 22px;
    fill: var(--red);
    flex: none;
  }
  .footer-band {
    position: absolute;
    left: 0;
    bottom: 0;
    width: 1080px;
    height: 140px;
  }
  .website {
    position: absolute;
    left: 0;
    bottom: 28px;
    width: 100%;
    text-align: center;
    color: #fff;
    font-size: 22px;
    margin: 0;
  }
</style>
</head>
<body>
  <main class="card">
    <header class="brand">
      <span class="brand-mark"></span>
      <h1 class="brand-name">Pepa Ruvel's Charred Relish</h1>
    </header>

    <section class="holder">
      <p class="holder-name">Howard Pellingham</p>
      <p class="holder-address">P. O Box 7413<br>Dunmore Vale, CA, 90417</p>
    </section>

    <div class="divider"></div>

    <ul class="contacts">
      <li>
        <svg viewBox="0 0 24 24" aria-hidden="true"><path d="M6.6 10.8a15 15 0 0 0 6.6 6.6l2.2-2.2c.3-.3.7-.4 1-.2 1.1.4 2.3.6 3.6.6.6 0 1 .4 1 1V20c0 .6-.4 1-1 1A17 17 0 0 1 3 4c0-.6.4-1 1-1h3.5c.6 0 1 .4 1 1 0 1.3.2 2.5.6 3.6.1.3 0 .7-.2 1z"/></svg>
        <span>(T) 855-PEPA-RUV (855-737-2788)</span>
      </li>
      <li>
        <svg viewBox="0 0 24 24" aria-hidden="true"><path d="M6.6 10.8a15 15 0 0 0 6.6 6.6l2.2-2.2c.3-.3.7-.4 1-.2 1.1.4 2.3.6 3.6.6.6 0 1 .4 1 1V20c0 .6-.4 1-1 1A17 17 0 0 1 3 4c0-.6.4-1 1-1h3.5c.6 0 1 .4 1 1 0 1.3.2 2.5.6 3.6.1.3 0 .7-.2 1z"/></svg>
        <span>949-555-0142</span>
      </li>
      <li>
        <svg viewBox="0 0 24 24" aria-hidden="true"><path d="M7 1h10a2 2 0 0 1 2 2v18a2 2 0 0 1-2 2H7a2 2 0 0 1-2-2V3a2 2 0 0 1 2-2zm0 3v14h10V4zm5 15.5a1.2 1.2 0 1 0 0 2.4 1.2 1.2 0 0 0 0-2.4z"/></svg>
        <span>949.555.0187</span>
      </li>
      <li>
        <svg viewBox="0 0 24 24" aria-hidden="true"><path d="M12 2a10 10 0 1 0 5 18.7l-1-1.7A8 8 0 1 1 20 12v1.2a1.8 1.8 0 0 1-3.6 0V7.5h-2v.9A5 5 0 1 0 15 16a3.8 3.8 0 0 0 7-2.8V12A10 10 0 0 0 12 2zm0 13a3 3 0 1 1 0-6 3 3 0 0 1 0 6z"/></svg>
        <span>howard@CharredRelish.com</span>
      </li>
    </ul>

    <svg class="footer-band" viewBox="0 0 1080 140" aria-hidden="true">
      <path d="M0 20 Q540 95 1080 20" fill="none" stroke="var(--green)" stroke-width="6"/>
      <path d="M0 38 Q540 112 1080 38 L1080 140 L0 140 Z" fill="var(--red)"/>
    </svg>
    <p class="website">www.CharredRelish.com</p>
  </main>
</body>
</html>
```